QBT Web Design Project

I would like a simple and elegant design for my international business consulting practice web site. I already have new QBT Logo and will have brochure-colors are blue, green and black

Practice areas:
I offer consulting services specializing in developing Internet-based anti-counterfeiting and anti-fraud programs, test purchases and investigations.

I offer Cyber Security, Data Protection and Compliance services

I also offer International Due Diligence Investigations and Country and Travel Risk Assessments

General Background Investigations

Physical Security Services

About me section listing my Bio

I have a set of key associates that I work with around the world and will want to list their CVs or Bios under "QBT

Associates"Banner with nice photo but not too cluttered

Ability to Upload documents and articles

Contact us section
Updates

I have uploaded my new logo-please advise if you didn't get it or it is not in the correct file format.

Thank you

Gordon

Hello Everyone,

Thank you for your submissions and ideas. I'm not sure about design only vs code. I understand that some of you do not do code-if not then please just provide design.

More about my business: see below link on Google docs to my brochure-this should help but don't use that phone number-see below.

https://files.example-docs.net/viewer?id=XK93PLQ7ZTR2MWN8&hl=en_US

 

Here are some details.

Contacts:

Gordon T. Vostrell, CPP

President

Vostrell and Partners, LLC

P.O. Box 47192

Gaithersburg, MD 20899

USA

web address:www.Vostrellandpartners.example (currently not working)

email:gord @vostrelland partners.example

Tel: 202-555-0147

I hope this is helpful. Gord

Reason: Sorry but during holiday period, have not had as much time to devote to this project. Thanks for your submissions.

Per my previous guidance, please keep designs simple and elegant and free from traditional security images with locks and chains-I prefer one or at most, two photos. Two colors- blue and green in addition to black for print. I want to present professional, corporate and international image. Thank you for your ideas nad submissions.

Gord

Target Market(s)

Law firms, large multi-national corporations, Security Industry

Industry/Entity Type

Business

Requirements
Must have
• Must have sections: (will provide text)

About QBT (will provide text)

Practice areas

Associates (will provide text)

Contact us

(it must also have ability to upload files and articles)
Should not have
• Old style fonts and symbols such as security badges, scales of justice, etc. I want a sleek and modern design.

```html
<!DOCTYPE html>
<html lang="en">
<head>
<meta charset="utf-8">
<title>QBT | Vostrell &amp; Partners, LLC</title>
<link href="https://fonts.googleapis.com/css2?family=Oswald:wght@300;400&family=Open+Sans:wght@400;600&family=Noto+Serif&display=swap" rel="stylesheet">
<style>
:root{
  --blue:#0a5aa0;
  --blue-dark:#084a86;
  --blue-light:#3aa3e6;
  --sky:#eaf3fa;
  --text:#444;
  --red:#d0021b;
  --grey:#e4e4e4;
  --yellow:#ffcc00;
  --line:#c8c8c8;
}
*{margin:0;padding:0;box-sizing:border-box}
html,body{width:932px;height:1200px;overflow:hidden;background:#fff}
body{position:relative;font-family:"Open Sans",Arial,sans-serif;color:var(--text);font-size:11px}
.abs{position:absolute}
a{text-decoration:none;color:inherit}

/* header */
.brand{left:11px;top:38px}
.brand-row{display:flex;align-items:center;gap:8px}
.brand-mark{font-size:32px;color:var(--blue);letter-spacing:-1px;padding-right:8px;border-right:1px solid #333;line-height:36px}
.brand-name{font-size:28px;color:#222}
.brand-tag{font-size:17.5px;letter-spacing:2.6px;color:var(--blue);margin-top:2px}
.share{top:14px;right:10px;display:flex;gap:5px}
.share span{border:1px solid #c9c9c9;border-radius:3px;background:#f4f4f4;font-size:10px;padding:2px 6px;color:#333}
.share span.hot{background:#e8623a;color:#fff;border-color:#e8623a}
.callme{right:30px;top:56px;font-family:Oswald,sans-serif;font-size:28px;color:var(--blue)}
.callme b{color:var(--red);font-weight:400;font-size:24px}

/* nav */
.nav{left:10px;top:136px;width:912px;height:40px;background:var(--blue);display:flex}
.nav a{color:#fff;font-size:13px;display:flex;align-items:center;justify-content:center;border-right:1px solid #2a74b6;height:100%}
.nav a:last-child{border:0}

/* sidebar */
.side{left:10px;top:184px;width:170px;background:var(--grey)}
.side a{display:block;height:29px;line-height:29px;padding-left:15px;font-size:12px;color:#444;border-bottom:2px solid #fff}
.side a:last-child{border:0;height:34px}
.banner{left:188px;top:184px;width:734px;height:243px;border:1px solid #bbb;padding:4px}
.banner-art{width:100%;height:100%;background:radial-gradient(circle at 26% 45%,#9fd3ef 0,#2d6f93 28%,#3a1111 55%,#000 78%)}
.banner-title{left:450px;top:26px;font-family:Oswald,sans-serif;font-weight:300;font-size:27px;line-height:34px;color:var(--yellow);width:290px}

/* feature strip */
.features{left:10px;top:437px;width:912px;height:175px;border:1px solid #bbb;background:linear-gradient(#f3f8fc,#e3edf5);display:flex}
.feature{flex:1;padding:14px 0 0 12px}
.feature-head{display:flex;align-items:center;gap:10px}
.feature-icon{width:32px;height:32px;border-radius:6px}
.feature h3{font-family:Oswald,sans-serif;font-weight:300;font-size:24px;color:var(--blue)}
.feature p{margin:14px 0 0 46px;font-size:12.5px;line-height:15.5px;color:#555;width:240px}
.more{display:block;margin:18px 0 0 46px;color:var(--red);font-size:10px}
.more::before{content:"\25B8 ";font-size:8px}

/* welcome */
.welcome{left:10px;top:638px;width:565px}
.welcome h1{font-family:"Noto Serif",serif;font-weight:400;font-size:17px;color:#333;padding-bottom:8px;border-bottom:1px dashed #aaa}
.welcome h1 span{color:var(--blue);font-size:22px}
.welcome p{margin-top:16px;font-size:10.8px;line-height:16.5px;color:#555}
.welcome .more{margin:24px 0 0 0}

/* clients */
.clients{left:618px;top:655px;width:306px;height:276px;background:#a9cde3;clip-path:polygon(0 0,94% 0,100% 3%,100% 100%,6% 100%,0 90%)}
.clients-inner{position:absolute;left:1px;top:1px;width:286px;height:250px;background:#fff;border:1px solid #9cc}
.clients-head{height:48px;margin:2px;background:linear-gradient(#5db8ef,var(--blue-light));display:flex;align-items:center;justify-content:space-between;padding:0 14px}
.clients-head h2{font-family:Oswald,sans-serif;font-weight:400;font-size:22px;color:#123}
.clients-head i{width:18px;height:16px;border:2px solid #345;display:block}
.clients ul{list-style:none;padding:10px 0 0 12px}
.clients li{height:27px;line-height:27px;font-size:12.5px;color:var(--blue);border-bottom:1px solid #3a4a5a;margin-right:0;padding-left:25px;position:relative}
.clients li::before{content:"\2726";position:absolute;left:0;color:var(--blue);font-size:9px}

/* lists */
.col{top:962px}
.col h2{font-family:"Noto Serif",serif;font-weight:400;font-size:17px;color:var(--blue);padding-bottom:10px;border-bottom:1px dashed #aaa}
.col ul{list-style:none;margin-top:12px}
.col li{font-size:11px;color:var(--blue-light);line-height:13px;margin-bottom:14px;padding-left:26px;position:relative}
.col li::before{content:"\00BB";position:absolute;left:8px;color:#777}
.docs{left:10px;width:269px}
.news{left:317px;width:229px}
.news .more{margin:-4px 0 0 4px}

.contact{left:658px;top:962px;width:260px}
.contact h2{font-family:Oswald,sans-serif;font-weight:300;font-size:24px;color:var(--blue);padding-bottom:6px;border-bottom:2px solid #e4e4e4}
.contact-row{display:flex;align-items:center;gap:8px;margin-top:6px}
.contact-phone{font-family:"Noto Serif",serif;font-size:22px;color:var(--blue)}
.contact-mail{font-family:"Noto Serif",serif;font-size:12.5px;color:var(--blue-dark)}
.social{display:flex;gap:18px;margin-top:12px;align-items:center}
.social span{display:flex;align-items:center;gap:6px;font-size:11px;color:var(--blue)}
.social i{width:28px;height:28px;background:var(--blue);border-radius:4px;display:block}

.footer{left:10px;top:1140px;width:912px;height:46px;background:var(--blue);color:#fff;font-size:11.5px;display:flex;align-items:center;justify-content:center;border:1px solid #084a86}
</style>
</head>
<body>

<header>
  <div class="abs brand">
    <div class="brand-row"><span class="brand-mark">QBT</span><span class="brand-name">Vostrell &amp; Partners, LLC</span></div>
    <div class="brand-tag">Intellectual Property and Cyber Security</div>
  </div>
  <div class="abs share"><span>Share</span><span>Post</span><span>0</span><span>+1</span><span>0</span><span>Like</span><span class="hot">Share</span></div>
  <div class="abs callme"><b>Call Me :</b> 202-555-0147</div>
</header>

<nav class="abs nav">
  <a href="#" style="width:113px">About Us</a>
  <a href="#" style="width:126px">Solutions</a>
  <a href="#" style="width:136px">Case Studies</a>
  <a href="#" style="width:96px">QBT</a>
  <a href="#" style="width:115px">Insights</a>
  <a href="#" style="width:121px">Careeres</a>
  <a href="#" style="width:96px">FAQs</a>
  <a href="#" style="width:109px">Contact Us</a>
</nav>

<aside class="abs side">
  <a href="#">Cybersecurity</a><a href="#">Cybersecurity Home</a><a href="#">Solutions</a><a href="#">Case Studies</a><a href="#">Insights</a><a href="#">Press Releases</a><a href="#">Public Sector</a><a href="#">Contact Cybersecurity</a>
</aside>

<section class="abs banner">
  <div class="banner-art" role="img" aria-label="Photo of a robotic hand touching a glowing digital globe"></div>
  <div class="abs banner-title">Data Loss Prevention, Cyber Security, Intellectual Property</div>
</section>

<section class="abs features">
  <div class="feature">
    <div class="feature-head"><svg class="feature-icon" viewBox="0 0 32 32"><path d="M16 2 L29 6 V16 C29 24 22 29 16 31 C10 29 3 24 3 16 V6 Z" fill="#5bbf3a"/><path d="M9 16 L14 21 L23 11" stroke="#fff" stroke-width="3.5" fill="none"/></svg><h3>Cyber Security</h3></div>
    <p>Lorem ipsum dolor sit amet, consectetur adipiscing elit. Suspendisse ut eleifend orci. Phasellus eu sem a lectus tempus congue a lacinia elit. Integer tincidunt,</p>
    <a class="more" href="#">Learn More</a>
  </div>
  <div class="feature">
    <div class="feature-head"><div class="feature-icon" style="background:#c9a54a" role="img" aria-label="Icon of a storage case"></div><h3>Data Protection</h3></div>
    <p>Lorem ipsum dolor sit amet, consectetur adipiscing elit. Suspendisse ut eleifend orci. Phasellus eu sem a lectus tempus congue a lacinia elit. Integer tincidunt,</p>
    <a class="more" href="#">Learn More</a>
  </div>
  <div class="feature">
    <div class="feature-head"><div class="feature-icon" style="background:#f2d23a" role="img" aria-label="Icon of a document with gears"></div><h3>Compliance services</h3></div>
    <p>Lorem ipsum dolor sit amet, consectetur adipiscing elit. Suspendisse ut eleifend orci. Phasellus eu sem a lectus tempus congue a lacinia elit. Integer tincidunt,</p>
    <a class="more" href="#">Learn More</a>
  </div>
</section>

<section class="abs welcome">
  <h1>Welcome to <span>QBT | Vostrell &amp; Partners, LLC</span></h1>
  <p>Integer suscipit, neque quis dignissim pellentesque, augue turpis auctor tortor, sed gravida arcu orci nec lectus. Cras sed rutrum magna. Proin nec augue neque, sed sagittis lacus. Lorem ipsum dolor sit amet, consectetur adipiscing elit. Aenean ornare, quam quis porttitor faucibus, augue mi vehicula elit, sed feugiat dui mauris a arcu. Suspendisse sit amet est sed sem tempor porta eu eget enim. Sed venenatis, magna id pretium luctus, nibh risus bibendum urna, vitae aliquet eros sapien ut est.</p>
  <p>Integer suscipit, neque quis dignissim pellentesque, augue turpis auctor tortor, sed gravida arcu orci nec lectus. Cras sed rutrum magna. Proin nec augue neque, sed sagittis lacus. Lorem ipsum dolor sit amet, consectetur adipiscing elit. Aenean ornare, quam quis porttitor faucibus, augue mi vehicula elit.</p>
  <p>Lorem ipsum dolor sit amet, consectetur adipiscing elit. Aenean ornare, quam quis porttitor faucibus, augue mi vehicula elit, sed feugiat dui mauris a arcu. Suspendisse sit amet est sed sem tempor porta eu eget enim. Sed venenatis, magna id pretium luctus, nibh risus bibendum urna, vitae aliquet eros sapien ut est.</p>
  <a class="more" href="#">Read More</a>
</section>

<section class="abs clients">
  <div class="clients-inner">
    <div class="clients-head"><h2>My Clients</h2><i></i></div>
    <ul><li>Client 1</li><li>Client 2</li><li>Client 3</li><li>Client 4</li><li>Client 5</li><li>Client 6</li></ul>
  </div>
</section>

<section class="abs col docs">
  <h2>Documentation</h2>
  <ul>
    <li>Lorem ipsum dolor sit amet, adipiscing elit.</li>
    <li>Integer ornare nulla sed leo posuere eu a sem.</li>
    <li>Ut sagittis nisi ac nunc molestie varius.</li>
    <li>Praesent cursus nisi iaculis ut sodales purus</li>
  </ul>
</section>

<section class="abs col news">
  <h2>Latest News</h2>
  <ul>
    <li>Lorem ipsum dolor sit amet, consectetur adipiscing elit.</li>
    <li>Integer ornare nulla sed leo posuere eu accumsan sem auctor.</li>
    <li>Ut sagittis nisi ac nunc molestie varius.</li>
  </ul>
  <a class="more" href="#">Read More News</a>
</section>

<section class="abs contact">
  <h2>Contact Us</h2>
  <div class="contact-row"><svg width="32" height="30" viewBox="0 0 32 30"><rect x="2" y="4" width="28" height="24" rx="6" fill="#f08a1c"/><path d="M10 10 c0 8 4 12 12 12 l2-3-4-2-2 2c-3-1-4-3-5-5l2-2-2-4z" fill="#fff"/></svg><span class="contact-phone">202-555-0147</span></div>
  <div class="contact-row"><svg width="32" height="26" viewBox="0 0 32 26"><rect x="3" y="5" width="26" height="17" rx="2" fill="#4aa6e0"/><path d="M3 6 L16 15 L29 6" stroke="#fff" stroke-width="2" fill="none"/></svg><span class="contact-mail">gord @vostrelland partners.example</span></div>
  <div class="social"><span><i></i>Friendbook</span><span><i style="background:#5bb8e8"></i>Chirper</span></div>
</section>

<footer class="abs footer">© 2011, All Rights Reserved</footer>

</body>
</html>
```